upmarket Hair salon A5 flyer design colour double sided

Phone number 9318 7061
address is shop 3/7 Marlowe pde Butler
Hi i am wanting a flyer that is upmarket and elegant for my hair salon Velvet Strands For Hair if any pics of hair must look great.
both side must have logo and contact details on
offer side 1
50% off
style cut and finish
*not valid Saturdays
*expires 31/03/15
*butler salon only
*not valid with any other offers
offer side 2
1/2 head foils or all over colour,
cut and finish
$120
*toners and treatment extra costs
*expires 31/03/15
*butler salon only

```html
<!DOCTYPE html>
<html lang="en">
<head>
<meta charset="utf-8">
<title>Velvet Strands For Hair – Flyer</title>
<link rel="stylesheet" href="https://fonts.googleapis.com/css2?family=Italianno&family=Parisienne&family=Arimo:wght@400&display=swap">
<style>
  :root {
    --paper: #ffffff;
    --slate: #4b4b49;
    --band-dark: #242424;
    --band-light: #323232;
    --mint: #d6e8a8;
    --sky: #a9d9ee;
    --salmon: #f27f7a;
    --amber: #f2a226;
    --rust: #b4521d;
    --ink-light: #ffffff;
  }
  * { box-sizing: border-box; margin: 0; padding: 0; }
  html, body {
    width: 1200px; height: 847px; overflow: hidden;
    background: var(--paper);
  }
  .flyer-sheet { position: relative; width: 1200px; height: 847px; }
  .flyer-side {
    position: absolute; top: 0; width: 592px; height: 847px; overflow: hidden;
    font-family: "Arimo", Arial, sans-serif;
  }
  .side-colour { left: 0; background: var(--slate); }
  .side-cut { left: 606px; background: var(--paper); }

  .stripe-band {
    position: absolute; left: 0; right: 0; top: 580px; bottom: 0;
    background: repeating-linear-gradient(90deg,
      var(--band-dark) 0 22px, var(--band-light) 22px 44px);
  }
  .hero-photo { position: absolute; }
  .side-colour .hero-photo {
    left: 120px; top: 0; width: 360px; height: 540px;
    border-radius: 45% 45% 40% 40%;
    background: linear-gradient(160deg, #3aa6de 0%, #4fc0c8 25%, #8cc53f 42%,
      #f2cf35 55%, #e8542c 70%, #d02f6e 85%, #7a3c92 100%);
    filter: blur(2px);
  }
  .side-cut .hero-photo {
    left: 180px; top: 0; width: 400px; height: 575px;
    background: radial-gradient(ellipse at 45% 28%, #e9822d 0%, #c85a1c 35%,
      #6d4a35 60%, #2e2a28 75%, rgba(255,255,255,0) 95%);
  }

  .brand-name {
    position: absolute; font-family: "Parisienne", cursive;
    font-weight: 400; white-space: nowrap; line-height: 1;
  }
  .side-colour .brand-name {
    top: 12px; left: 0; width: 100%; text-align: center;
    font-size: 44px; color: var(--mint);
  }
  .side-cut .brand-name {
    top: 594px; left: 140px; font-size: 40px; color: var(--amber);
  }

  .offer-title {
    position: absolute; left: 0; top: 420px; width: 592px; height: 180px;
    overflow: visible;
  }
  .offer-title text {
    font-family: "Italianno", cursive; font-size: 170px;
  }
  .side-colour .offer-title text { fill: var(--sky); }
  .side-cut .offer-title text { fill: var(--amber); }

  .offer-subtitle {
    position: absolute; right: 12px; top: 578px;
    font-size: 21px; color: var(--ink-light);
  }
  .price {
    position: absolute; left: 338px; top: 616px;
    font-size: 88px; color: var(--salmon); line-height: 1;
  }
  .price-rule {
    position: absolute; left: 340px; top: 704px; width: 200px; height: 5px;
    background: var(--sky);
  }
  .discount {
    position: absolute; left: 0; top: 0; width: 300px; height: 440px;
    overflow: visible;
  }
  .discount text {
    font-family: "Arimo", Arial, sans-serif; font-size: 58px; fill: var(--rust);
  }
  .discount line { stroke: var(--amber); stroke-width: 4; }

  .contact {
    position: absolute; left: 18px; top: 700px; font-style: normal;
    color: var(--ink-light); font-size: 21px; line-height: 1.3;
  }
  .terms {
    position: absolute; top: 764px; left: 326px; list-style: none;
    color: var(--salmon); font-size: 14px; line-height: 1.25;
  }
  .terms li::before { content: "- "; }
</style>
</head>
<body>
<main class="flyer-sheet">

  <section class="flyer-side side-colour">
    <div class="hero-photo" role="img" aria-label="Photo of long hair dyed in bright rainbow colours, rolled into an updo, seen from behind"></div>
    <div class="stripe-band"></div>
    <h2 class="brand-name">Velvet Strands For Hair</h2>
    <svg class="offer-title" viewBox="0 0 592 180" aria-label="All Over Colour">
      <text x="8" y="140" textLength="576" lengthAdjust="spacingAndGlyphs">All Over Color</text>
    </svg>
    <p class="offer-subtitle">or half head foils, cut and finish</p>
    <p class="price">$120</p>
    <div class="price-rule"></div>
    <address class="contact">9318 7061<br>3/7 Marlowe Pde Butler</address>
    <ul class="terms">
      <li>tone and treatment extra costs</li>
      <li>expires 31/03/15</li>
      <li>butler salon only</li>
      <li>not valid with any other offers</li>
    </ul>
  </section>

  <section class="flyer-side side-cut">
    <div class="hero-photo" role="img" aria-label="Photo of a model with a short, textured copper-orange haircut"></div>
    <div class="stripe-band"></div>
    <svg class="discount" viewBox="0 0 300 440" aria-label="50% off">
      <g transform="rotate(-35 24 390)">
        <text x="24" y="390">50%off</text>
        <line x1="30" y1="408" x2="270" y2="408"/>
      </g>
    </svg>
    <svg class="offer-title" viewBox="0 0 592 180" aria-label="Style Cut Finish">
      <text x="8" y="140" textLength="576" lengthAdjust="spacingAndGlyphs">Style Cut Finish</text>
    </svg>
    <h2 class="brand-name">Velvet Strands For Hair</h2>
    <address class="contact">9318 7061<br>3/7 Marlowe Pde Butler</address>
    <ul class="terms">
      <li>not vaild Saturday</li>
      <li>expires 31/03/15</li>
      <li>butler salon only</li>
      <li>not valid with any other offers</li>
    </ul>
  </section>

</main>
</body>
</html>
```